Pedicure Menu with 8 Scent Options

This design will be for a single page menu (front/back) that will display multiple different scent variations of a product. The purpose of this menu is to display to clients and show them the available options and benefits of each option.
The menu will be double sided.
The front page will include a header including brand logo and product name, and a total of 8 different scents including imagery and descriptive text.
The design should include the text provided for each scent. The design should have a layout that is structured/organized, easy to read, and has bright imagery that represents each scent.
An example is a modular layout using boxes that highlight a different scent within each box. Lavender scent should include aesthetic images of lavender flower and/or the color purple.
The back page will include brand logo, overall product description, and additional brief text that explains each step of the product.
The final size of the design should be 8.5"x11", produced in InDesign format, with all layers editable for future changes.
NOTE: Please carefully review the attached design brief that includes additional information, and all necessary text to include in the design.
Target Market(s)
Beauty/Spa Clients
Industry/Entity Type
Beauty
Requirements
Must have
- Bright and Vivid Imagery/Illustrations
Nice to have
- Background design that utilizes, lines, shapes, or other elements.

```html
<!DOCTYPE html>
<html lang="en">
<head>
<meta charset="utf-8">
<title>Lumeya Deluxe Pedicure 4-Step Menu</title>
<link href="https://fonts.googleapis.com/css2?family=Fira+Sans:wght@400;500;600;700&family=Lora:ital,wght@1,500&family=Oswald:wght@500&display=swap" rel="stylesheet">
<style>
  :root{
    --backdrop:#d4d4d4;
    --paper:#ffffff;
    --ink:#111111;
    --header:#050505;
    --swirl:#ececec;
    --frame:#a8b84a;
    --pill-top:#d6e07a;
    --pill-bottom:#9fb13c;
    --lavender:#7b4f9f;
    --mandarin:#e2782a;
    --jasmine:#bcc4a8;
    --greentea:#9dc05e;
    --cucumber:#178a40;
    --rose:#d77b86;
    --honey:#f4cb38;
    --mint:#8ec742;
  }
  *{box-sizing:border-box;margin:0;padding:0}
  html,body{width:1200px;height:1200px;overflow:hidden}
  body{background:var(--backdrop);font-family:"Fira Sans",sans-serif;color:var(--ink);position:relative}
  .page{position:absolute;top:248px;width:540px;height:705px;background:var(--paper);overflow:hidden}
  .page--front{left:40px}
  .page--back{left:620px}
  .page-swirl{position:absolute;inset:0;width:100%;height:100%}
  .page-header{position:absolute;left:0;top:0;width:100%;height:82px;background:var(--header);display:flex;align-items:center;justify-content:center}
  .brand-name{font-family:"Fira Sans",sans-serif;font-weight:500;font-size:34px;color:#fff;letter-spacing:1px;display:flex;align-items:center;gap:8px}
  .brand-dot{width:8px;height:8px;border-radius:50%;background:#fff}
  .title-pill{position:absolute;left:172px;top:68px;width:196px;height:28px;border-radius:6px;background:linear-gradient(var(--pill-top),var(--pill-bottom));border:1.5px solid #7f8f2a;display:flex;align-items:center;justify-content:center;font-size:16px;font-weight:500;color:#1a1a1a}
  .pick-heading{position:absolute;left:0;width:100%;top:101px;text-align:center;font-weight:700;font-size:13px;letter-spacing:1.5px}
  .scent-card{position:absolute;width:210px;height:88px;background:var(--tone);border:2px solid var(--frame);border-radius:5px}
  .scent-art{position:absolute;left:-2px;top:-38px;width:84px;height:126px;border-radius:4px;background:linear-gradient(160deg,var(--light),var(--tone))}
  .scent-name{position:absolute;left:86px;top:2px;font-family:"Lora",serif;font-style:italic;font-weight:500;font-size:15px;color:#fff}
  .scent-text{position:absolute;left:86px;top:22px;width:112px;height:54px;background:#fff;border-radius:2px;padding:2px 3px;font-size:4.6px;line-height:1.4;text-align:justify;color:#222}
  .intro{position:absolute;left:14px;right:14px;top:90px;text-align:center;font-size:14.5px;line-height:1.25;font-weight:400}
  .step{position:absolute;width:192px;text-align:center}
  .step-photo{width:192px;height:159px;border:3px solid var(--frame);border-radius:7px;position:relative;background:var(--shade)}
  .step-number{position:absolute;right:-3px;top:-3px;width:34px;height:36px;background:linear-gradient(var(--pill-top),var(--pill-bottom));border-radius:0 7px 0 10px;color:#fff;font-family:"Oswald",sans-serif;font-size:24px;line-height:36px;text-align:center}
  .step-title{margin-top:6px;font-weight:600;font-size:14px;letter-spacing:.3px}
  .step-text{font-size:13.5px;line-height:1.1;padding:0 22px}
  .contact{position:absolute;left:36px;top:629px;width:150px}
  .contact-row{display:flex;align-items:center;gap:8px}
  .contact-phone{font-family:"Oswald",sans-serif;font-size:23px;letter-spacing:.5px}
  .contact-address{font-size:8.5px;font-style:italic;line-height:1.2}
  .web{position:absolute;left:194px;top:637px;width:312px;text-align:center}
  .web-label{font-size:11px;letter-spacing:1.2px;font-weight:500}
  .web-pill{margin-top:2px;height:27px;border-radius:5px;background:linear-gradient(var(--pill-top),var(--pill-bottom));border:1.5px solid #7f8f2a;font-size:17px;font-weight:500;line-height:24px;letter-spacing:.3px}
</style>
</head>
<body>

<section class="page page--front">
  <svg class="page-swirl" viewBox="0 0 540 705" aria-hidden="true">
    <path d="M40 705 C20 560 30 330 200 200 C320 110 480 150 520 300 C560 460 470 620 380 705 Z M200 705 C150 560 240 460 360 470 C300 560 300 640 330 705 Z" fill="var(--swirl)" fill-rule="evenodd"/>
  </svg>
  <header class="page-header"><span class="brand-name">Lumeya<span class="brand-dot"></span></span></header>
  <div class="title-pill">Deluxe Pedicure 4-Step</div>
  <div class="pick-heading">PICK YOUR PEDICURE</div>

  <div class="scent-card" style="left:42px;top:177px;--tone:var(--lavender);--light:#c6a9dd">
    <div class="scent-art" role="img" aria-label="Illustration of lavender sprigs"></div>
    <div class="scent-name">Lavender</div>
    <p class="scent-text">Melt away the stresses of the day with a delicate, sweet smell that is floral and woodsy at the same time. Lavender is a calming scent for relaxation that puts us in a better mood and helps create a sense of tranquility and peacefulness.</p>
  </div>
  <div class="scent-card" style="left:288px;top:177px;--tone:var(--mandarin);--light:#9fcf6a">
    <div class="scent-art" role="img" aria-label="Illustration of a mandarin branch with fruit and blossoms"></div>
    <div class="scent-name">Mandarin</div>
    <p class="scent-text">Uplift your senses with a fruity and sweet aroma that promotes clarity, radiance and a smooth, even skin tone. A citrus blend of essential oils works great to polish dull skin, reduce wrinkles, and correct spots.</p>
  </div>
  <div class="scent-card" style="left:42px;top:316px;--tone:var(--jasmine);--light:#f6f1e2">
    <div class="scent-art" role="img" aria-label="Illustration of white jasmine flowers"></div>
    <div class="scent-name">Jasmine</div>
    <p class="scent-text">Embrace the warmth of a rich and sensual floral scent that boosts your energy levels and helps make your day better and brighter. A symbol of purity, love, and beauty – Jasmine helps to reduce exhaustion, nervousness, and stress.</p>
  </div>
  <div class="scent-card" style="left:288px;top:316px;--tone:var(--greentea);--light:#c9e68e">
    <div class="scent-art" role="img" aria-label="Illustration of green tea leaves"></div>
    <div class="scent-name">Green Tea</div>
    <p class="scent-text">Restore a sense of serenity with fragrant green tea extract that helps to relax the mind, reduces redness and swelling, and leaves the skin feeling hydrated, silky, and smooth. A natural detoxification that will supplies abundant moisture to the skin.</p>
  </div>
  <div class="scent-card" style="left:42px;top:454px;--tone:var(--cucumber);--light:#f3d357">
    <div class="scent-art" role="img" aria-label="Illustration of cucumber vine and melon"></div>
    <div class="scent-name">Cucumber-Melon</div>
    <p class="scent-text">Jump into a refreshing blend of crisp cucumber, watery honeydew, and summer cantaloupe. Perfect for capturing the essence of a summer day. Bamboo and aloe extract help cool your skin after a day in the sun.</p>
  </div>
  <div class="scent-card" style="left:288px;top:454px;--tone:var(--rose);--light:#a9c86a">
    <div class="scent-art" role="img" aria-label="Illustration of pink roses on a stem"></div>
    <div class="scent-name">Rose</div>
    <p class="scent-text">Fall in love with a delicate floral twist of spicy and sweet that nourishes your skin and calms the mind. Essential oils help to reduce fine lines and protect the skin from UV damage.</p>
  </div>
  <div class="scent-card" style="left:42px;top:593px;--tone:var(--honey);--light:#f9f3e6">
    <div class="scent-art" role="img" aria-label="Illustration of honeycomb with a milk splash"></div>
    <div class="scent-name">Milk &amp; Honey</div>
    <p class="scent-text">Discover one of nature's most luxurious skin cleansers and softeners. Creamy milk is full of rich essential vitamins that supply abundant moisture and improves skin elasticity. Sweet honey contains antioxidants and other nutrients that slow down skin aging.</p>
  </div>
  <div class="scent-card" style="left:288px;top:593px;--tone:var(--mint);--light:#d3ee9f">
    <div class="scent-art" role="img" aria-label="Illustration of mint leaves"></div>
    <div class="scent-name">Mint</div>
    <p class="scent-text">Rejuvenate your body with a cool mix of peppermint and spearmint that prevents skin damage, alleviates inflamed skin, and acts as a splash of tonic for the senses. Infused with eucalyptus to leave you clean, cool, and crisp.</p>
  </div>
</section>

<section class="page page--back">
  <svg class="page-swirl" viewBox="0 0 540 705" aria-hidden="true">
    <path d="M0 300 C30 170 200 140 300 190 C440 250 520 380 490 520 C460 640 360 690 260 705 L0 705 Z M120 560 C110 470 200 430 270 470 C330 510 300 600 240 640 C180 650 130 620 120 560 Z" fill="var(--swirl)" fill-rule="evenodd"/>
  </svg>
  <header class="page-header"><span class="brand-name">Lumeya<span class="brand-dot"></span></span></header>
  <p class="intro">Lumeya Deluxe Pedicure 4-Step will transform your pedicure experience and immerse your senses into a floral paradise designed to rejuvenate your body. Sit back, relax, and enjoy.</p>

  <div class="step" style="left:63px;top:159px">
    <div class="step-photo" role="img" aria-label="Photo of feet soaking in a copper basin" style="--shade:linear-gradient(#8a5a3a,#c08a55)"><span class="step-number">1</span></div>
    <div class="step-title">SALT SOAK</div>
    <div class="step-text">Detoxifies and deodorizes your feet.</div>
  </div>
  <div class="step" style="left:285px;top:159px">
    <div class="step-photo" role="img" aria-label="Photo of hands scrubbing a leg" style="--shade:linear-gradient(135deg,#f4f2f2,#e3b894)"><span class="step-number">2</span></div>
    <div class="step-title">SUGAR SCRUB</div>
    <div class="step-text">Gently exfoliates dead skin.</div>
  </div>
  <div class="step" style="left:63px;top:388px">
    <div class="step-photo" role="img" aria-label="Photo of legs covered in a textured masque" style="--shade:linear-gradient(135deg,#c18a63,#d9c8bd)"><span class="step-number">3</span></div>
    <div class="step-title">FOOT MASQUE</div>
    <div class="step-text">Cleanses pores for smoother skin.</div>
  </div>
  <div class="step" style="left:285px;top:388px">
    <div class="step-photo" role="img" aria-label="Photo of hands massaging lotion into a leg" style="--shade:linear-gradient(135deg,#9b8a9a,#d4a07a)"><span class="step-number">4</span></div>
    <div class="step-title">MASSAGE LOTION</div>
    <div class="step-text">Hydrates and soothes skin.</div>
  </div>

  <div class="contact">
    <div class="contact-row">
      <svg width="20" height="20" viewBox="0 0 20 20" aria-hidden="true"><rect width="20" height="20" rx="4" fill="#111"/><path d="M6 4.5l2 .3 1 3-1.4 1.2a8 8 0 0 0 3.4 3.4l1.2-1.4 3 1 .3 2c-.2.8-1 1.5-2 1.5A11 11 0 0 1 4.5 6.5c0-1 .7-1.8 1.5-2z" fill="#fff"/></svg>
      <span class="contact-phone">XXX-XXX-XXX</span>
    </div>
    <div class="contact-row">
      <svg width="20" height="22" viewBox="0 0 20 22" aria-hidden="true"><rect width="20" height="22" rx="4" fill="#111"/><path d="M10 3.5a5 5 0 0 1 5 5c0 3.5-5 9-5 9s-5-5.5-5-9a5 5 0 0 1 5-5z" fill="#fff"/><circle cx="10" cy="8.5" r="2" fill="#111"/></svg>
      <span class="contact-address">Lorem ipsum dolor sit amet,<br>consectetuer adipiscing elit.</span>
    </div>
  </div>
  <div class="web">
    <div class="web-label">VISIT OUR WEBSITE</div>
    <div class="web-pill">www.BlueCoveRetail.com</div>
  </div>
</section>

</body>
</html>
```